Rooted Ready Rising: Quiet Roots, Open Doors, Steady Hands

I want a modern and clean looking book cover. 5.25x8

Title
Rooted Ready Rising

Subtitle
Quiet Roots, Open Doors, Steady Hands

I don’t just want a graphic, I want it to make sense. If it can just be the words and a textured looking background, I’ll be ok with that too. I just want it to look crisp, clean, modern.

I want the back to have my book blurb and bio attached with the pic that’s attached.

Target Market(s)

Self help

Requirements
Must have
• Modern, clean look, look professional, attract customers.

```html
<!DOCTYPE html>
<html lang="en">
<head>
<meta charset="utf-8">
<title>Rooted Ready Rising – Cover Concepts</title>
<link href="https://fonts.googleapis.com/css2?family=Exo+2:ital,wght@0,800;0,900;1,900&family=Mulish:ital,wght@1,400&family=Quicksand:wght@400&display=swap" rel="stylesheet">
<style>
  :root{
    --stage:#b5b5b5;
    --royal:#1f3a8f;
    --teal:#00658e;
    --orange:#dc6027;
    --rose:#cf8593;
    --navy:#0f2744;
    --charcoal:#3a3a3a;
    --crimson:#c21d33;
    --white:#ffffff;
    --ink:#1c1c1c;
    --photo-dark:#1e1e1e;
    --photo-light:#f1eeee;
  }
  *{margin:0;padding:0;box-sizing:border-box}
  html,body{width:1200px;height:1081px;overflow:hidden;background:var(--stage)}
  .board{position:relative;width:1200px;height:1081px}

  /* front cover component (base 365 x 555) */
  .cover{position:absolute;width:216.7px;height:329.6px;overflow:hidden;background:var(--bg);
         box-shadow:4px 6px 10px rgba(0,0,0,.35)}
  .cover .art{position:absolute;left:0;top:0;width:365px;height:555px;transform:scale(.5938);transform-origin:0 0}
  .art .hero-art{position:absolute;left:47px;top:95px;width:101px;height:310px;background:var(--fig)}
  .art .title-word{position:absolute;font-family:"Exo 2",sans-serif;font-weight:900;font-style:italic;
                   font-size:38px;line-height:1;color:var(--white);letter-spacing:-.5px;white-space:nowrap}
  .art .w1{left:160px;top:262px}
  .art .w2{left:160px;top:306px}
  .art .w3{left:160px;top:350px}
  .art .rule{position:absolute;left:47px;width:210px;height:3px;background:var(--accent)}
  .art .r1{top:414px}
  .art .r2{top:491px}
  .art .subtitle{position:absolute;left:47px;width:210px;top:423px;text-align:center;
                 font-family:"Exo 2",sans-serif;font-weight:800;font-size:15.5px;line-height:21px;color:var(--white)}
  .art .author{position:absolute;left:47px;width:210px;top:498px;text-align:center;
               font-family:"Exo 2",sans-serif;font-weight:800;font-size:14.5px;color:var(--accent)}

  .c-royal-orange{--bg:var(--royal);--accent:var(--orange);--fig:var(--orange)}
  .c-royal-rose{--bg:var(--royal);--accent:var(--rose);--fig:var(--rose)}
  .c-teal-orange{--bg:var(--teal);--accent:var(--orange);--fig:var(--orange)}
  .c-teal-rose{--bg:var(--teal);--accent:var(--rose);--fig:var(--rose)}
  .c-teal-navy{--bg:var(--teal);--accent:var(--navy);--fig:var(--navy)}
  .c-char-orange{--bg:var(--charcoal);--accent:var(--orange);--fig:var(--orange)}
  .c-char-crimson{--bg:var(--charcoal);--accent:var(--crimson);--fig:var(--crimson)}
  .c-rose-crimson{--bg:var(--rose);--accent:var(--crimson);--fig:var(--crimson)}

  /* full wrap */
  .wrap{position:absolute;left:33px;top:395px;width:908px;height:631px;overflow:hidden;
        background:var(--rose);box-shadow:4px 6px 10px rgba(0,0,0,.35)}
  .wrap .front{position:absolute;left:492px;top:0;width:365px;height:555px;transform:scale(1.146);transform-origin:0 0}
  .back-heading{position:absolute;left:27px;font-family:"Mulish",sans-serif;font-style:italic;font-weight:400;
                font-size:15.5px;color:var(--ink)}
  .blurb-heading{top:30px}
  .bio-heading{top:252px}
  .copy{position:absolute;left:27px;font-family:"Quicksand",sans-serif;font-size:8.3px;line-height:10.5px;color:var(--white)}
  .blurb{top:60px;width:365px}
  .bio{top:280px;width:198px}
  .author-photo{position:absolute;left:234px;top:243px;width:163px;height:336px;border-radius:70px 70px 30px 30px;
                background:linear-gradient(180deg,var(--photo-dark) 0%,var(--photo-dark) 48%,var(--photo-light) 52%,var(--photo-light) 95%,var(--crimson) 100%)}
  .spine-art{position:absolute;left:432px;top:31px;width:57px;height:24px;background:var(--crimson);border-radius:4px}
  .spine-text{position:absolute;font-family:"Exo 2",sans-serif;font-weight:900;color:var(--crimson);
              writing-mode:vertical-rl;white-space:nowrap;line-height:1}
  .spine-title{left:441px;top:80px;font-size:23px}
  .spine-author{left:443px;top:410px;font-size:21px}
</style>
</head>
<body>
<div class="board">

  <div class="cover c-royal-orange" style="left:33px;top:33px">
    <div class="art">
      <div class="hero-art" role="img" aria-label="Cover artwork: a figure standing on a tall column"></div>
      <div class="title-word w1">ROOTED</div><div class="title-word w2">READY</div><div class="title-word w3">RISING</div>
      <div class="rule r1"></div>
      <p class="subtitle">Quiet Roots,<br>Open Doors,<br>Steady Hands</p>
      <div class="rule r2"></div>
      <p class="author">Marisol Keane</p>
    </div>
  </div>

  <div class="cover c-royal-rose" style="left:262px;top:33px">
    <div class="art">
      <div class="hero-art" role="img" aria-label="Cover artwork: a figure standing on a tall column"></div>
      <div class="title-word w1">ROOTED</div><div class="title-word w2">READY</div><div class="title-word w3">RISING</div>
      <div class="rule r1"></div>
      <p class="subtitle">Quiet Roots,<br>Open Doors,<br>Steady Hands</p>
      <div class="rule r2"></div>
      <p class="author">Marisol Keane</p>
    </div>
  </div>

  <div class="cover c-teal-orange" style="left:492px;top:33px">
    <div class="art">
      <div class="hero-art" role="img" aria-label="Cover artwork: a figure standing on a tall column"></div>
      <div class="title-word w1">ROOTED</div><div class="title-word w2">READY</div><div class="title-word w3">RISING</div>
      <div class="rule r1"></div>
      <p class="subtitle">Quiet Roots,<br>Open Doors,<br>Steady Hands</p>
      <div class="rule r2"></div>
      <p class="author">Marisol Keane</p>
    </div>
  </div>

  <div class="cover c-teal-rose" style="left:721px;top:33px">
    <div class="art">
      <div class="hero-art" role="img" aria-label="Cover artwork: a figure standing on a tall column"></div>
      <div class="title-word w1">ROOTED</div><div class="title-word w2">READY</div><div class="title-word w3">RISING</div>
      <div class="rule r1"></div>
      <p class="subtitle">Quiet Roots,<br>Open Doors,<br>Steady Hands</p>
      <div class="rule r2"></div>
      <p class="author">Marisol Keane</p>
    </div>
  </div>

  <div class="cover c-teal-navy" style="left:951px;top:33px">
    <div class="art">
      <div class="hero-art" role="img" aria-label="Cover artwork: a figure standing on a tall column"></div>
      <div class="title-word w1">ROOTED</div><div class="title-word w2">READY</div><div class="title-word w3">RISING</div>
      <div class="rule r1"></div>
      <p class="subtitle">Quiet Roots,<br>Open Doors,<br>Steady Hands</p>
      <div class="rule r2"></div>
      <p class="author">Marisol Keane</p>
    </div>
  </div>

  <div class="cover c-char-orange" style="left:951px;top:375px">
    <div class="art">
      <div class="hero-art" role="img" aria-label="Cover artwork: a figure standing on a tall column"></div>
      <div class="title-word w1">ROOTED</div><div class="title-word w2">READY</div><div class="title-word w3">RISING</div>
      <div class="rule r1"></div>
      <p class="subtitle">Quiet Roots,<br>Open Doors,<br>Steady Hands</p>
      <div class="rule r2"></div>
      <p class="author">Marisol Keane</p>
    </div>
  </div>

  <div class="cover c-char-crimson" style="left:951px;top:718px">
    <div class="art">
      <div class="hero-art" role="img" aria-label="Cover artwork: a figure standing on a tall column"></div>
      <div class="title-word w1">ROOTED</div><div class="title-word w2">READY</div><div class="title-word w3">RISING</div>
      <div class="rule r1"></div>
      <p class="subtitle">Quiet Roots,<br>Open Doors,<br>Steady Hands</p>
      <div class="rule r2"></div>
      <p class="author">Marisol Keane</p>
    </div>
  </div>

  <div class="wrap c-rose-crimson">
    <h2 class="back-heading blurb-heading">Rooted Ready Rising</h2>
    <p class="copy blurb">Everyone has big dreams and lofty goals, but few give themselves permission to try.<br>
    Rooted Ready Rising: Quiet Roots, Open Doors, Steady Hands is for anyone who has ever been stymied by negative self-talk, maltreatment, troubles at home, relationship problems, or has experienced anything significant that has made you want to abandon your dreams.<br>
    Part memoir, part self-help book, part spiritual guide, this book aims to provide encouragement and a helping hand to anyone who feels like life has passed them by or think their time will never come.<br>
    Inside, you’ll find deeply personal stories and anecdotes from Author Marisol Keane. Her personal experiences provide a detailed account and roadmap for how to lift yourself out of a dark spot, find your voice, dream bigger, dare to try, and change your life for the better.<br>
    If you’ve ever felt like where you are now is where you’ll always be or fear that your prayers will never be answered, this book will help you move past obstacles, shatter expectations, and learn how to confidently bet on yourself because you’re worth it.<br>
    Scroll up and click “Add to cart” to find the support and motivation you need to move forward in life and finally be who you were meant to be!</p>

    <h2 class="back-heading bio-heading">Marisol Keane</h2>
    <p class="copy bio">is a helper. For as long as she can remember, she’s always wanted to do the right thing, but life, circumstance, and some very tough years, set her on a path that conflicted with what was in her heart… until something clicked and she made herself and her goals a priority.<br>
    A dreamer and visionary at her core, she knows all too well how much faith and courage it takes to defy expectations and build your own path forward. Her tenacity led her in a direction that would change her life for the better.<br>
    After being told she wasn’t “college material” in high school, she made it her mission to never allow anyone to define who she is, and more importantly, to empower others to do the same. Today, the devout Christian, Author, Motivator, Coach, Educator, and Educational Leader, holds 3 degrees (Bachelors of Science in Psychology, Master of Education, and Educational Specialist) and is currently in the dissertation phase of a Doctorate of Education. Recently, she added Life Coach to her resume.<br>
    When she’s not teaching, studying, coaching, reading, writing, listening to music, or helping others achieve their goals, she spends as much time as she can with her loving husband, three beautiful daughters, her college aged God-daughter, and countless friends.</p>

    <div class="author-photo" role="img" aria-label="Full-length photo of the author in a black tee, white jeans and red heels"></div>

    <div class="spine-art" role="img" aria-label="Small spine artwork of a standing figure, turned sideways"></div>
    <div class="spine-text spine-title">Rooted Ready Rising</div>
    <div class="spine-text spine-author">Marisol Keane</div>

    <div class="art front">
      <div class="hero-art" role="img" aria-label="Cover artwork: a figure standing on a tall column"></div>
      <div class="title-word w1">ROOTED</div><div class="title-word w2">READY</div><div class="title-word w3">RISING</div>
      <div class="rule r1"></div>
      <p class="subtitle">Quiet Roots,<br>Open Doors,<br>Steady Hands</p>
      <div class="rule r2"></div>
      <p class="author">Marisol Keane</p>
    </div>
  </div>

</div>
</body>
</html>
```